Fun, Clean Business Card For Family Focused Travel Agency

I need a business card using specific colors and fonts as in the uploaded files. Ideally, I would like a large image of the logo on the back and all the contact info on the front. Maybe the stars/dots somewhere in a flowy form.

I do want it the contact information to be clear and easy to read. I don't want it to look too busy. Maybe even a bit minimalist.

I plan or ordering the ROUNDED CORNER business cards from Cardwell Press, so please consider that in your design.

Target Market(s)

Families with children, couples, groups of friends

Contact Information for Business Card

Marla Quent, Owner
Marla@TidewayTrips.example
Cell Phone Number 555-218-6034
Office Phone Number 555-647-1295
Specializing in Fablecrest destinations, Goldmere Parkside Resort, Cruises and All-Inclusive Vacations.

Nice but not required:
www.TidewayTrips.example
Facebook, Instagram, Twitter icons with username: TidewayTrips

Font styles to use
Sans Serif

Requirements
Must have
• Please try to use the colors from the logo as much as possible. I understand lighter shades/colors may be needed for some things.
Should not have
• NO SERIF FONTS. That is really the only thing I do not want at all

```html
<!DOCTYPE html>
<html lang="en">
<head>
<meta charset="utf-8">
<title>Tideway Trips – Business Card</title>
<link rel="stylesheet" href="https://fonts.googleapis.com/css2?family=Titillium+Web:wght@400;600;700&display=swap">
<style>
  :root {
    --navy: #0f1336;
    --ink: #1b1d2a;
    --teal: #1bb59a;
    --paper: #ffffff;
    --backdrop: #e9eaee;
    --muted: #4a4d5c;
  }
  * { box-sizing: border-box; margin: 0; padding: 0; }
  html, body {
    width: 1200px; height: 786px; overflow: hidden;
    background: var(--backdrop);
    font-family: "Titillium Web", sans-serif;
  }
  .sheet {
    width: 1200px; height: 786px;
    display: flex; align-items: center; justify-content: center; gap: 60px;
  }
  .card {
    width: 525px; height: 300px;
    border-radius: 22px;
    position: relative;
    box-shadow: 0 10px 30px rgba(15, 19, 54, 0.18);
  }
  .card--front { background: var(--paper); color: var(--ink); }
  .card--back { background: var(--navy); display: flex; align-items: center; justify-content: center; }

  .holder { position: absolute; left: 38px; top: 34px; }
  .holder__name { font-weight: 700; font-size: 17px; letter-spacing: 0.02em; text-transform: uppercase; }
  .holder__role { font-size: 13px; color: var(--muted); margin-top: -3px; }

  .contacts { position: absolute; left: 38px; top: 110px; list-style: none; }
  .contacts li { display: flex; align-items: center; gap: 8px; font-size: 13.5px; line-height: 21px; }
  .contacts svg { width: 13px; height: 13px; flex: none; }
  .socials { display: flex; gap: 3px; }
  .socials span { width: 12px; height: 12px; border-radius: 2px; background: var(--teal); display: block; }

  .brand { display: flex; align-items: center; gap: 10px; }
  .brand__dot { border-radius: 50%; background: var(--teal); flex: none; }
  .brand__name { font-weight: 700; line-height: 1; }
  .card--front .brand { position: absolute; right: 40px; top: 118px; }
  .card--front .brand__dot { width: 34px; height: 34px; }
  .card--front .brand__name { font-size: 30px; color: var(--navy); }
  .card--back .brand__dot { width: 64px; height: 64px; }
  .card--back .brand__name { font-size: 56px; color: var(--paper); }

  .specialty {
    position: absolute; right: 40px; bottom: 30px;
    text-align: right; font-size: 13px; line-height: 18px; color: var(--ink);
  }
</style>
</head>
<body>
<main class="sheet">
  <section class="card card--front" aria-label="Card front">
    <header class="holder">
      <h1 class="holder__name">Marla Quent</h1>
      <p class="holder__role">Owner</p>
    </header>
    <ul class="contacts">
      <li>
        <svg viewBox="0 0 16 16" aria-hidden="true"><rect x="4" y="1" width="8" height="14" rx="2" fill="none" stroke="var(--teal)" stroke-width="2"/></svg>
        555-218-6034
      </li>
      <li>
        <svg viewBox="0 0 16 16" aria-hidden="true"><path d="M3 2h3l1.5 3.5-2 1.2a8 8 0 0 0 3.8 3.8l1.2-2L14 10v3a1.5 1.5 0 0 1-1.5 1.5A11.5 11.5 0 0 1 1.5 3.5 1.5 1.5 0 0 1 3 2z" fill="var(--teal)"/></svg>
        555-647-1295
      </li>
      <li>
        <svg viewBox="0 0 16 16" aria-hidden="true"><rect x="1" y="3" width="14" height="10" rx="1.5" fill="var(--teal)"/><path d="M1.5 4l6.5 5 6.5-5" fill="none" stroke="#fff" stroke-width="1.4"/></svg>
        Marla@TidewayTrips.example
      </li>
      <li>
        <svg viewBox="0 0 16 16" aria-hidden="true"><circle cx="8" cy="8" r="6.5" fill="none" stroke="var(--teal)" stroke-width="1.5"/><path d="M1.5 8h13M8 1.5c-3 3.5-3 9.5 0 13M8 1.5c3 3.5 3 9.5 0 13" fill="none" stroke="var(--teal)" stroke-width="1.2"/></svg>
        www.TidewayTrips.example
      </li>
      <li>
        <span class="socials" aria-hidden="true"><span></span><span></span><span></span></span>
        /TidewayTrips
      </li>
    </ul>
    <div class="brand">
      <span class="brand__dot" aria-hidden="true"></span>
      <span class="brand__name">Tideway Trips</span>
    </div>
    <p class="specialty">
      Specializing in Fablecrest destinations,<br>
      Goldmere Parkside Resort,<br>
      Cruises and All-Inclusive Vacations.
    </p>
  </section>

  <section class="card card--back" aria-label="Card back">
    <div class="brand">
      <span class="brand__dot" aria-hidden="true"></span>
      <span class="brand__name">Tideway Trips</span>
    </div>
  </section>
</main>
</body>
</html>
```